Business Recognition Design

We need a design for a recognition to be given to business leaders in our community.
The recognition shall be made on a brass plaque on wood panel background (picture attached, please use it as a background), and all drawing must be in vectors and only one color (black).
It should also have a logo on the top and signature on the right bottom.
The text is enclosed in DOC file.
Updates

Reason: just to be able to find the best solution

Reason: None of the suggestion is good enough. Logo in general is too big in comparison with the rest of the plate.

Industry/Entity Type

Business

Requirements
Must have
• - standard Windows font (or possibility to install the same font on Windows), as the name on the recognition shall be printed in the same font
Nice to have
• - some graphic element (in curves) representing achievements in business
- should look great :)

```html
<!DOCTYPE html>
<html lang="de">
<head>
<meta charset="utf-8">
<title>Auszeichnung – Unternehmer des Jahres</title>
<link rel="stylesheet" href="https://fonts.googleapis.com/css2?family=Arimo:wght@400;700&display=swap">
<style>
  :root {
    --stage: #3a3a3a;
    --wood-dark: #4a2a18;
    --wood-mid: #6b3f24;
    --wood-light: #7d4b2c;
    --brass-light: #f3dc7a;
    --brass-mid: #d9b443;
    --brass-deep: #b8902a;
    --engrave: #1c1608;
    --ornament: rgba(40, 28, 6, 0.22);
    --screw-light: #fff3b0;
    --screw-dark: #8a6a1c;
  }
  * { margin: 0; padding: 0; box-sizing: border-box; }
  html, body { width: 1200px; height: 832px; overflow: hidden; }
  body {
    background: var(--stage);
    font-family: "Arimo", Arial, sans-serif;
    position: relative;
  }
  .plaque-board {
    position: absolute;
    left: 162px; top: 33px;
    width: 876px; height: 672px;
    background: linear-gradient(135deg, var(--wood-light), var(--wood-mid) 45%, var(--wood-dark));
    border-radius: 4px;
  }
  .brass-plate {
    position: absolute;
    left: 33px; top: 27px;
    width: 810px; height: 618px;
    background: linear-gradient(160deg, var(--brass-light) 0%, var(--brass-mid) 40%, var(--brass-light) 62%, var(--brass-deep) 100%);
    color: var(--engrave);
    text-align: center;
  }
  .ornament-frame { position: absolute; left: 0; top: 0; width: 810px; height: 618px; }
  .screw {
    position: absolute;
    width: 18px; height: 18px;
    border-radius: 50%;
    background: radial-gradient(circle at 35% 35%, var(--screw-light), var(--brass-mid) 55%, var(--screw-dark));
  }
  .screw.tl { left: 16px; top: 16px; }
  .screw.tr { right: 16px; top: 16px; }
  .screw.bl { left: 16px; bottom: 16px; }
  .screw.br { right: 16px; bottom: 16px; }
  .plate-content { position: absolute; left: 0; top: 0; width: 810px; height: 618px; }
  .brand {
    position: absolute; top: 120px; left: 0; width: 100%;
    display: flex; justify-content: center; align-items: center; gap: 8px;
    font-weight: 700; font-size: 30px;
  }
  .brand-mark { width: 16px; height: 16px; background: var(--engrave); }
  .line { position: absolute; left: 0; width: 100%; line-height: 1; }
  .title { top: 218px; font-size: 47px; letter-spacing: 1px; }
  .subtitle { font-size: 27px; font-weight: 700; }
  .subtitle.one { top: 288px; }
  .subtitle.two { top: 328px; }
  .for { top: 367px; font-size: 17px; }
  .honoree { top: 390px; font-size: 25px; font-weight: 700; }
  .body-text { font-size: 17px; }
  .body-text.one { top: 425px; }
  .body-text.one strong { font-size: 19px; }
  .body-text.one small { font-size: 12px; font-weight: 700; }
  .body-text.two { top: 448px; }
  .body-text.three { top: 471px; }
  .footer { position: absolute; top: 555px; font-size: 19px; }
  .footer.place { left: 228px; }
  .footer.signer { left: 480px; }
</style>
</head>
<body>
  <div class="plaque-board">
    <div class="brass-plate">
      <svg class="ornament-frame" viewBox="0 0 810 618" role="img" aria-label="Barockes Rankenornament als Rahmen um den Text">
        <path fill="var(--ornament)" fill-rule="evenodd"
          d="M40 40 H770 V590 H40 Z M120 75 H690 Q690 80 690 100 V530 H120 V100 Q120 80 120 75 Z"/>
      </svg>
      <span class="screw tl"></span><span class="screw tr"></span>
      <span class="screw bl"></span><span class="screw br"></span>
      <div class="plate-content">
        <div class="brand"><span class="brand-mark"></span><span class="brand-name">TradeCrest</span></div>
        <div class="line title">AUSZEICHNUNG</div>
        <div class="line subtitle one">als herausragendster Unternehmer</div>
        <div class="line subtitle two">Deutschlands 2013</div>
        <div class="line for">für</div>
        <div class="line honoree">Herrn Dipl.-Kfm. Max Muster</div>
        <div class="line body-text one">Unter der Leitung von <strong>Herr Dipl.-Kfm.</strong> <small>Max Muster</small></div>
        <div class="line body-text two">hat sich die FIRMA GmbH im Jahr 2013 unter den ersten 5% der</div>
        <div class="line body-text three">größten deutschen Wirtschaftsunternehmen platziert.</div>
        <div class="footer place">Gilching, 20. Juni 2013</div>
        <div class="footer signer">Clara Vogel</div>
      </div>
    </div>
  </div>
</body>
</html>
```